Quellbyte Business cards template

We're looking for something modern and elegant. We are a reseller of technology (computers, datacenter, etc). Color theme would be "only" white with the incorporation of the blue that's present on our website (Quellbyte.com) and logo file. We would like for the card to provide all the necessary info for the specific person (Phone#, fax#, email, name, website URL) . I'm attaching the logo file to this request. Please have it show Montreal/New York somewhere, without providing specific addresses.

Target Market(s)

All b2b

Industry/Entity Type

Business

Contact Information for Business Card

Please have the color scheme be represented by only the white and blue from our website (Quellbyte.com) and logo. We would like to logo on the card, but not big and overwhelming. This card will be used as a template for anybody within the company, it should display the user's name, phone#, fax#, email, job title and website URL. Please have it show Montreal/New York somewhere, without providing our specific addresses. Really, we're looking for a clean, simple and elegant look.

Font styles to use
Serif

Requirements
Must have
• Please see card details
Nice to have
• Please see card details
Should not have
• Anything tacky or tagline.

```html
<!DOCTYPE html>
<html lang="en">
<head>
<meta charset="utf-8">
<title>Quellbyte Business Cards</title>
<link rel="stylesheet" href="https://fonts.googleapis.com/css2?family=Source+Serif+4:wght@400;600;800&display=swap">
<style>
  :root {
    --brand-blue: #0a7acb;
    --deep-blue: #0b5fb0;
    --card-white: #ffffff;
    --ink-grey: #5a5f66;
    --backdrop: #e9ebee;
  }
  * { margin: 0; padding: 0; box-sizing: border-box; }
  html, body { width: 1200px; height: 1200px; overflow: hidden; }
  body {
    background: var(--backdrop);
    font-family: "Source Serif 4", Georgia, serif;
    position: relative;
  }
  .card {
    position: absolute;
    left: 250px;
    width: 700px;
    height: 400px;
    background: var(--card-white);
    box-shadow: 0 6px 18px rgba(0,0,0,0.12);
    overflow: hidden;
  }
  .card--front { top: 150px; }
  .card--back { top: 650px; }

  .wordmark {
    color: var(--brand-blue);
    font-weight: 400;
    letter-spacing: 0.5px;
    display: flex;
    align-items: center;
    gap: 14px;
    line-height: 1;
  }
  .wordmark__dot {
    width: 16px; height: 16px;
    border-radius: 50%;
    background: var(--brand-blue);
    flex: none;
  }
  .card--front .wordmark {
    position: absolute;
    left: 48px; top: 72px;
    font-size: 54px;
  }
  .holder {
    position: absolute;
    left: 330px; top: 146px;
    text-align: right;
    width: 300px;
  }
  .holder__name {
    color: var(--deep-blue);
    font-weight: 800;
    font-size: 32px;
    letter-spacing: 0.5px;
    line-height: 1.1;
  }
  .holder__title {
    color: var(--ink-grey);
    font-size: 16px;
    margin-top: 4px;
  }
  .holder__cities {
    color: var(--brand-blue);
    font-size: 14px;
    letter-spacing: 1px;
    margin-top: 4px;
  }
  .rule {
    position: absolute;
    left: 0; right: 0;
    top: 246px;
    height: 2px;
    background: var(--brand-blue);
  }
  .contact-band {
    position: absolute;
    left: 0; right: 0; top: 258px; bottom: 0;
    background: var(--brand-blue);
    color: var(--card-white);
    display: flex;
    flex-direction: column;
    justify-content: center;
    align-items: center;
    font-size: 18px;
    letter-spacing: 0.4px;
  }
  .contact-band__line { padding: 8px 0; white-space: nowrap; }
  .contact-band__divider {
    width: 560px; height: 1px;
    background: rgba(255,255,255,0.7);
  }
  .card--back .wordmark {
    position: absolute;
    left: 0; right: 0; top: 0; bottom: 0;
    justify-content: center;
    font-size: 72px;
  }
</style>
</head>
<body>
  <section class="card card--front" aria-label="Business card front">
    <div class="wordmark"><span class="wordmark__dot"></span>Quellbyte</div>
    <div class="holder">
      <div class="holder__name">ELISE VARNER</div>
      <div class="holder__title">Director</div>
      <div class="holder__cities">Montreal | New York</div>
    </div>
    <div class="rule"></div>
    <div class="contact-band">
      <div class="contact-band__line">T: 1-800-555-QELB (7352) | F: 1-800-555 (7353)</div>
      <div class="contact-band__divider"></div>
      <div class="contact-band__line">W: www.quellbyte.com | E: info@quellbyte.com</div>
    </div>
  </section>

  <section class="card card--back" aria-label="Business card back">
    <div class="wordmark"><span class="wordmark__dot"></span>Quellbyte</div>
  </section>
</body>
</html>
```